Real Estate Agent need For Sale sign for

We need a for sale sign for our team based in Los Angeles, CA. My team name is Corvalen Real Estate Group. Also known as Team Corvalen. We are also under the Brandt Osgood umbrella. We are a real estate team that enjoys contributing to the world through supporting homeowners and sellers achieve their real estate goals. The final design should communicate trust, integrity, and loyalty.
Need to have our team name on there: Team Corvalen, phone number 323-555-0172, my licensed number DRE #8062714 on there. The size of the sign will be 32X36.
Target Market(s)
Home buyers and sellers.
Industry/Entity Type
Real Estate Agent
Colors
Designer to choose colors to be used in the design.
Look and feel

```html
<!DOCTYPE html>
<html lang="en">
<head>
<meta charset="utf-8">
<title>Team Corvalen – For Sale Sign</title>
<link rel="stylesheet" href="https://fonts.googleapis.com/css2?family=Roboto:wght@300;400;700;900&display=swap">
<style>
  :root {
    --canvas: #eeeeee;
    --brand-red: #c8102e;
    --band-red-light: #b3121f;
    --band-red-dark: #6e0a12;
    --ink: #000000;
    --paper: #ffffff;
    --tagline-grey: #5a5a5a;
    --stripe-silver: #d9d9d9;
  }
  html, body {
    margin: 0;
    padding: 0;
    width: 800px;
    height: 1200px;
    overflow: hidden;
    background: var(--canvas);
  }
  .canvas {
    position: relative;
    width: 800px;
    height: 1200px;
  }
  .sign {
    position: absolute;
    left: 40px;
    top: 195px;
    width: 720px;
    height: 810px;
    background: var(--paper);
    box-shadow: 0 6px 24px rgba(0,0,0,0.18);
    font-family: 'Roboto', Arial, sans-serif;
    overflow: hidden;
  }
  .sign-bands {
    position: absolute;
    inset: 0;
  }
  .headline {
    position: absolute;
    left: 0;
    top: 22px;
    width: 720px;
    margin: 0;
    text-align: center;
    color: var(--paper);
    font-weight: 900;
    font-size: 128px;
    line-height: 1;
    letter-spacing: 1px;
  }
  .team-name {
    position: absolute;
    left: 50px;
    top: 262px;
    margin: 0;
    color: var(--brand-red);
    font-weight: 900;
    line-height: 1;
  }
  .team-name .line-team {
    display: flex;
    align-items: center;
    gap: 22px;
    font-size: 112px;
  }
  .team-name .mark {
    width: 40px;
    height: 40px;
    background: var(--brand-red);
  }
  .team-name .line-surname {
    display: block;
    font-size: 106px;
    margin-top: 8px;
    letter-spacing: -1px;
  }
  .tagline {
    position: absolute;
    left: 0;
    top: 530px;
    width: 720px;
    margin: 0;
    text-align: center;
    color: var(--tagline-grey);
    font-weight: 400;
    font-size: 48px;
    line-height: 1;
  }
  .contact {
    position: absolute;
    left: 0;
    top: 590px;
    width: 720px;
    height: 220px;
    text-align: center;
    color: var(--paper);
  }
  .contact .phone {
    display: block;
    margin-top: 12px;
    font-weight: 900;
    font-size: 88px;
    line-height: 1;
    letter-spacing: 1px;
  }
  .contact .license {
    display: block;
    margin-top: 14px;
    font-weight: 700;
    font-size: 34px;
    line-height: 1;
  }
  .contact .brokerage {
    display: block;
    margin-top: 14px;
    font-weight: 400;
    font-size: 34px;
    line-height: 1;
    text-transform: uppercase;
    letter-spacing: 1px;
  }
</style>
</head>
<body>
<main class="canvas">
  <section class="sign" aria-label="For sale yard sign">
    <svg class="sign-bands" width="720" height="810" viewBox="0 0 720 810" aria-hidden="true">
      <defs>
        <linearGradient id="headerRed" x1="0" y1="0" x2="0" y2="1">
          <stop offset="0" stop-color="var(--band-red-dark)"/>
          <stop offset="0.55" stop-color="var(--band-red-light)"/>
          <stop offset="1" stop-color="var(--band-red-dark)"/>
        </linearGradient>
        <linearGradient id="stripeSheen" x1="0" y1="0" x2="1" y2="0">
          <stop offset="0" stop-color="#000"/>
          <stop offset="0.5" stop-color="var(--stripe-silver)"/>
          <stop offset="1" stop-color="#000"/>
        </linearGradient>
      </defs>
      <polygon class="header-band" points="0,0 720,0 720,196 0,239" fill="url(#headerRed)"/>
      <polygon class="header-stripe" points="0,239 720,196 720,208 0,255" fill="url(#stripeSheen)"/>
      <rect class="contact-band" x="0" y="590" width="720" height="220" fill="var(--ink)"/>
    </svg>

    <h1 class="headline">FOR SALE</h1>

    <p class="team-name">
      <span class="line-team">Team <span class="mark" aria-hidden="true"></span></span>
      <span class="line-surname">CORVALEN</span>
    </p>

    <p class="tagline">Your Realtor for life</p>

    <div class="contact">
      <span class="phone">323-555-0172</span>
      <span class="license">DRE #8062714</span>
      <span class="brokerage">Brandt Osgood</span>
    </div>
  </section>
</main>
</body>
</html>
```